Upscale Children's Boutique Needs a PSD Web Design

We need a PSD web design for an online children's boutique called 'Mavoret'. We specialize in special occasion wear for infants. Our apparel products are typically selected for christening & baptisms, birthdays, holidays and weddings. We would like to see designs that compliment our existing logo and business card. The final design should communicate a sense of luxury, but also be fun and oriented towards children.
Our current website is www.mavoret.com. Note: Not all products are loaded.
Changes to the color scheme, fonts, background and graphics are welcome. And while we like the layout of my current TrellaCart theme (Seashore), we do expect that SMALL modifications will be needed to make it ours. For example, we would like the cart to be placed more visibly. I have a designer that can code the changes you come up with so feel free to suggest what you feel is best.
We look forward to your designs. Good luck!
Websites we like:
https://www.shopwrenfig.com/ (The layout of this site is nice to me)
http://www.elsiesattic.com/
http://www.quietmeadowherbals.com/
Updates
This contest is for PSD design only. No Trellacart development or coding is required.
Target Market(s)
Our typical customer is female age 20-45 shopping for her own child or for a gift.
Industry/Entity Type
Boutique
Requirements
Must have
- PSD Design
- These 5 items listed below are things we’d like:
- (1) General styling (color scheme, fonts, background, graphics, etc.) & layout
- • ONLY the logo colors are set … feel free to add colors that compliment it
- • Prefer narrow (or single line) footer
- • We think the main banner/image is too large
- (2) Create main banner/image (current template uses 970px wide)
- (3) AT LEAST Three (3) Marketing banners (current template uses 433 x 225):
- • Our Hottest Products
- • Our Newest Arrivals
- • Newsletter sign-up
- (4) Border to enclose admin links (My account, Gift Certificates, Create an Account)
- (5) New badges / icon / images
- • Shopping Cart --> Bag or cart image should stand out; try to place above search bar (you’ll have to lower the search bar to do this)
- • Sale Badge --> anything goes. Could be a badge or a sash. Might also be nice to have these for the bestsellers as well.
- • Star Icons for product reviews (optional) --> Keep the stars just have them be more stylized
Nice to have
- We like pages that have a background and think one might look good on our site if not too busy.
Should not have
- We do not like extremely dark backgrounds for web pages.

```html
<!DOCTYPE html>
<html lang="en">
<head>
<meta charset="utf-8">
<title>Mavoret Childrenswear</title>
<link href="https://fonts.googleapis.com/css2?family=Josefin+Sans:wght@400;600;700&family=Montserrat:wght@400;600;700&family=Great+Vibes&display=swap" rel="stylesheet">
<style>
:root{
  --teal:#3aaba6;
  --teal-dark:#2c8f8b;
  --teal-pale:#e3f7f7;
  --peach:#f7a98a;
  --peach-soft:#f9c2ab;
  --purple:#a530d6;
  --pink:#f6b6cc;
  --page:#eef1f1;
  --ink:#3b3b3b;
  --white:#fff;
}
*{box-sizing:border-box;margin:0;padding:0}
html,body{width:728px;height:1200px;overflow:hidden}
body{position:relative;background:var(--page);font-family:"Montserrat",sans-serif;color:var(--ink)}
.abs{position:absolute}

.topbar{left:0;top:0;width:728px;height:17px;background:var(--teal)}
.social{left:118px;top:5px;display:flex;gap:17px}
.social span{width:7px;height:7px;border-radius:50%;background:var(--white);opacity:.85}
.admin-links{left:364px;top:5px;display:flex;gap:11px;font-size:4.8px;color:var(--white);letter-spacing:.2px;white-space:nowrap}

.header{left:0;top:17px;width:728px;height:101px;background:var(--white)}
.join{left:160px;top:40px;font-family:"Josefin Sans",sans-serif;font-size:9.5px;color:var(--peach);letter-spacing:.4px}
.join b{font-weight:400;margin:0 2px}
.logo{left:302px;top:30px;display:flex;align-items:center;gap:6px}
.logo .dot{flex-shrink:0;width:14px;height:14px;border-radius:50%;background:var(--teal)}
.logo .name{font-family:"Josefin Sans",sans-serif;font-size:27px;color:var(--teal);letter-spacing:1px;line-height:1}
.logo-sub{left:338px;top:67px;font-family:"Josefin Sans",sans-serif;font-size:6.5px;color:var(--teal);letter-spacing:1.3px}
.icon-search{left:466px;top:32px}
.icon-cart{left:508px;top:33px}
.cart-count{left:544px;top:28px;width:15px;height:15px;border-radius:50%;background:var(--peach);border:1.5px solid var(--white);box-shadow:0 0 0 1px var(--peach);color:var(--white);font-size:7px;text-align:center;line-height:12px}

.nav{left:114px;top:82px;width:490px;height:30px;border-top:1px solid var(--teal);border-bottom:1px solid var(--teal)}
.nav a{position:absolute;top:8px;font-family:"Josefin Sans",sans-serif;font-size:11.6px;font-weight:600;color:var(--teal-dark);text-decoration:none;white-space:nowrap;line-height:1}
.nav a.active{top:3px;height:22px;padding:5px 12px 0 12px;background:var(--peach-soft)}

.hero{left:114px;top:120px;width:490px;height:166px;background:linear-gradient(90deg,#f7bcd0,#f4a8c4 55%,#f19fbd)}
.hero-photo{left:370px;top:120px;width:234px;height:166px;
  background:
   radial-gradient(ellipse 34% 30% at 50% 86%,#fff 0,#fbeff3 45%,rgba(255,255,255,0) 100%),
   radial-gradient(ellipse 14% 16% at 48% 60%,#f9a9c6 0,#f7b9cf 60%,rgba(247,185,207,0) 100%),
   radial-gradient(ellipse 15% 14% at 50% 42%,#fffdfd 0,#f6eef0 60%,rgba(255,255,255,0) 100%),
   radial-gradient(ellipse 11% 13% at 50% 16%,#f6dccd 0,#e9c3ae 60%,rgba(233,195,174,0) 100%),
   linear-gradient(90deg,rgba(247,184,204,0),#f6b3ca 30%,#f7c4d4)}
.hero-title{left:188px;top:152px;width:160px;text-align:center;font-weight:700;font-size:40px;line-height:1;color:var(--purple);letter-spacing:.5px}
.hero-sub{left:188px;top:200px;width:160px;text-align:center;font-family:"Great Vibes",cursive;font-size:32px;line-height:1;color:var(--purple)}
.hero-rule{height:1.5px;background:var(--purple);opacity:.7}

.perks{left:114px;top:286px;width:490px;height:44px;background:var(--teal);display:flex}
.perk{flex:1;text-align:center;padding-top:7px;font-family:"Josefin Sans",sans-serif;color:var(--white)}
.perk h3{font-size:10.5px;font-weight:600;letter-spacing:1px;line-height:1.1}
.perk p{font-size:6px;letter-spacing:1px;opacity:.7;margin-top:2px}
.perk i{display:block;width:46px;height:1px;background:rgba(255,255,255,.5);margin:6px auto 0}

.promos{left:113px;top:338px;width:492px;height:84px;background:var(--teal);padding:3px;display:flex;gap:6px}
.promo{flex:1;position:relative;overflow:hidden}
.promo-1{background:
  radial-gradient(ellipse 20% 34% at 80% 86%,#1f2f4a 0,#2b3b58 50%,rgba(43,59,88,0) 100%),
  radial-gradient(ellipse 32% 40% at 80% 90%,#fff 0,#f3eef0 60%,rgba(255,255,255,0) 100%),
  radial-gradient(ellipse 8% 14% at 80% 24%,#f2d6c4 0,rgba(242,214,196,0) 100%),
  linear-gradient(90deg,#fff 0,#fde6ee 45%,#f5b1c8)}
.promo-2{background:
  radial-gradient(ellipse 40% 22% at 50% 96%,#f0468f 0,#f46aa4 50%,rgba(244,106,164,0) 100%),
  radial-gradient(ellipse 26% 32% at 50% 78%,#fff 0,#f6eef0 60%,rgba(255,255,255,0) 100%),
  radial-gradient(ellipse 20% 34% at 50% 36%,#f4d2be 0,#e6b196 55%,rgba(230,177,150,0) 100%),
  linear-gradient(90deg,#f9c8d8,#f3a3bf)}
.promo-3{background:
  radial-gradient(ellipse 8% 36% at 80% 80%,#f0358d 0,rgba(240,53,141,0) 100%),
  radial-gradient(ellipse 30% 40% at 80% 90%,#fff 0,#f4eef2 60%,rgba(255,255,255,0) 100%),
  radial-gradient(ellipse 7% 13% at 80% 22%,#f2d6c4 0,rgba(242,214,196,0) 100%),
  linear-gradient(90deg,#fde3ea,#f6b6cc)}
.promo-text{position:absolute;left:6px;top:22px;font-weight:700;font-size:20px;color:#d456b8;line-height:1}
.promo-script{position:absolute;font-family:"Great Vibes",cursive;font-size:19px;line-height:1;white-space:nowrap}
.badge-sale{position:absolute;width:38px;height:38px;border-radius:50%;text-align:center;color:var(--white);font-size:6px;line-height:1.05;padding-top:9px;font-weight:700}
.badge-sale b{font-size:8px;display:block}

.section-title{left:114px;width:490px;text-align:center;font-family:"Josefin Sans",sans-serif;font-weight:600;font-size:11px;letter-spacing:1.3px;color:var(--teal-dark)}
.section-rule{left:114px;width:490px;height:1px;background:var(--teal)}
.arrow{width:12px;height:11px;background:var(--teal);color:var(--white);font-size:8px;text-align:center;line-height:11px}

.card{width:112px;height:190px;background:var(--white)}
.card .photo{position:absolute;left:4px;top:4px;width:104px;height:126px}
.ph-dress{background:
  radial-gradient(ellipse 30% 20% at 50% 24%,#efe3cf 0,#f6efe4 55%,rgba(255,255,255,0) 100%),
  radial-gradient(ellipse 44% 40% at 50% 62%,#fff 0,#efeae2 55%,rgba(239,234,226,0) 100%),
  linear-gradient(180deg,#fbfbfb,#ededed)}
.ph-bootie{background:
  radial-gradient(ellipse 26% 18% at 36% 62%,#fff 0,#e2e2e2 70%,rgba(226,226,226,0) 100%),
  radial-gradient(ellipse 28% 20% at 64% 46%,#fff 0,#dedede 70%,rgba(222,222,222,0) 100%),
  linear-gradient(180deg,#fbfbfb,#f1f1f1)}
.ph-bib{background:
  radial-gradient(ellipse 36% 32% at 50% 60%,#fdfdfd 0,#ebebeb 70%,rgba(235,235,235,0) 100%),
  linear-gradient(180deg,#fbfbfb,#f0f0f0)}
.ph-sash{background:
  radial-gradient(ellipse 12% 26% at 62% 62%,#f5b9c8 0,rgba(245,185,200,0) 100%),
  radial-gradient(ellipse 40% 38% at 50% 68%,#fff 0,#ecebeb 60%,rgba(236,235,235,0) 100%),
  radial-gradient(ellipse 16% 16% at 50% 26%,#fbf7f7 0,rgba(251,247,247,0) 100%),
  linear-gradient(180deg,#fbfbfb,#efefef)}
.ph-suit{background:
  radial-gradient(ellipse 28% 40% at 50% 56%,#fff 0,#e9e9e9 60%,rgba(233,233,233,0) 100%),
  radial-gradient(ellipse 14% 12% at 50% 12%,#f7f7f7 0,rgba(247,247,247,0) 100%),
  linear-gradient(180deg,#fbfbfb,#f0f0f0)}
.card .stars{position:absolute;right:5px;top:134px;font-size:5px;letter-spacing:1px;color:var(--teal)}
.card .name{position:absolute;left:4px;top:145px;font-size:4.6px;color:#555;letter-spacing:.2px}
.card .desc{position:absolute;left:4px;top:152px;font-size:4.6px;color:#b5b5b5}
.card .price{position:absolute;right:4px;top:145px;font-size:7.5px;font-weight:600;color:var(--teal-dark)}
.card .wish{position:absolute;left:4px;top:168px;width:22px;height:17px;background:var(--teal)}
.card .wish svg{position:absolute;left:7px;top:5px}
.card .add{position:absolute;left:30px;top:168px;width:79px;height:17px;border:1px solid var(--teal);font-size:5.5px;font-weight:600;letter-spacing:.6px;color:var(--teal-dark);text-align:center;line-height:15px}

.overlay{position:absolute;left:4px;top:4px;width:104px;height:126px;background:#8d8473}
.ov-btn{position:absolute;left:40px;width:24px;height:24px;border-radius:50%;border:2px solid var(--white)}
.ov-btn svg{position:absolute;left:5px;top:5px}
.ov-label{position:absolute;left:0;width:104px;text-align:center;font-size:4.5px;font-weight:700;color:var(--white)}
.sash{position:absolute;left:4px;top:4px;width:42px;height:42px;overflow:hidden}
.sash span{position:absolute;left:-18px;top:12px;width:80px;height:10px;background:var(--teal);color:var(--white);font-size:4.5px;text-align:center;line-height:10px;transform:rotate(-45deg)}

.newsletter{left:108px;top:942px;width:490px;height:96px;background:var(--teal-pale)}
.newsletter p{position:absolute;left:0;top:26px;width:490px;text-align:center;font-family:"Josefin Sans",sans-serif;font-size:10px;font-weight:600;letter-spacing:.5px;color:#333}
.email{position:absolute;left:73px;top:44px;width:242px;height:30px;border:1px solid var(--teal);background:var(--teal-pale);font-family:"Josefin Sans",sans-serif;font-size:11px;color:#8a8a8a;padding:9px 6px 0;letter-spacing:.5px}
.signup{position:absolute;left:315px;top:44px;width:100px;height:30px;background:var(--teal);color:var(--white);font-family:"Josefin Sans",sans-serif;font-size:11px;text-align:center;line-height:32px}

.footer{left:0;top:1038px;width:728px;height:162px;background:var(--teal)}
.fcol{position:absolute;top:40px;font-family:"Josefin Sans",sans-serif;color:var(--white)}
.fcol h4{font-size:9.5px;font-weight:600;letter-spacing:.8px;margin-bottom:5px}
.fcol li{list-style:none;font-size:7px;line-height:15px;opacity:.85;letter-spacing:.4px}
</style>
</head>
<body>
<div class="abs topbar"></div>
<div class="abs social"><span></span><span></span><span></span><span></span></div>
<div class="abs admin-links"><span>MY ACCOUNT</span><span>GIFT CERTIFICATES</span><span>CREATE AN ACCOUNT</span><span>CALL (555) 214-7730</span></div>

<div class="abs header"></div>
<div class="abs join">JOIN<b>|</b>SIGN IN</div>
<div class="abs logo"><span class="dot"></span><span class="name">Mavoret</span></div>
<div class="abs logo-sub">CHILDRENSWEAR</div>
<svg class="abs icon-search" width="26" height="26" viewBox="0 0 26 26"><circle cx="10" cy="10" r="7" fill="none" stroke="var(--teal)" stroke-width="2.2"/><path d="M15 15l8 8" stroke="var(--peach)" stroke-width="3.5" stroke-linecap="round"/></svg>
<svg class="abs icon-cart" width="32" height="26" viewBox="0 0 32 26"><path d="M9 10 L14 2 M23 10 L18 2" stroke="var(--peach)" stroke-width="2" fill="none"/><rect x="2" y="9" width="28" height="4" rx="1" fill="var(--teal)"/><path d="M4 13h24l-3 11H7z" fill="none" stroke="var(--teal)" stroke-width="2"/><path d="M10 15v7M14 15v7M18 15v7M22 15v7" stroke="var(--teal)" stroke-width="1.6"/></svg>
<div class="abs cart-count">1</div>

<nav class="abs nav">
  <a style="left:2px">NEW BABY</a>
  <a style="left:89px">CHRISTENING &amp; BAPTISM</a>
  <a style="left:266px">BIRTHDAY</a>
  <a class="active" style="left:337px">HOLIDAY</a>
  <a style="left:427px">WEDDING</a>
</nav>

<div class="abs hero"></div>
<div class="abs hero-photo" role="img" aria-label="Smiling little girl in a white tulle dress with a pink sash"></div>
<div class="abs hero-rule" style="left:206px;top:146px;width:124px"></div>
<div class="abs hero-title">SPRING</div>
<div class="abs hero-sub">Sale</div>
<div class="abs hero-rule" style="left:248px;top:248px;width:40px"></div>
<div class="abs perks">
  <div class="perk"><h3>FREE SHIPPING</h3><p>ON ORDERS $49 &amp; UP</p><i></i></div>
  <div class="perk"><h3>EASY RETURNS</h3><p>FOR UP TO 60 DAYS</p><i></i></div>
  <div class="perk"><h3>SECURE SHOPPING</h3><p>SHOP WITH CONFIDENCE</p><i></i></div>
</div>

<div class="abs promos">
  <div class="promo promo-1" role="img" aria-label="Girl in a white tulle dress with a navy bow">
    <div class="promo-text">SPECIAL</div>
    <div class="promo-script" style="left:28px;top:46px;color:#b35fc4">Offer</div>
  </div>
  <div class="promo promo-2" role="img" aria-label="Young girl in a white dress with a pink bow">
    <div class="badge-sale" style="left:4px;top:4px;background:#36d3dc">SALE!<b>20%</b>OFF</div>
  </div>
  <div class="promo promo-3" role="img" aria-label="Girl in a tulle gown with a pink sash">
    <div class="promo-script" style="left:8px;top:30px;color:#7a4da8">Last Minute</div>
    <div class="promo-script" style="left:28px;top:54px;color:#d46aa0">Deals</div>
  </div>
</div>

<div class="abs section-title" style="top:439px">OUR HOTTEST PRODUCTS</div>
<div class="abs arrow" style="left:578px;top:438px">‹</div>
<div class="abs arrow" style="left:595px;top:438px">›</div>
<div class="abs section-rule" style="top:456px"></div>

<div class="abs card" style="left:115px;top:470px">
  <div class="photo ph-dress" role="img" aria-label="White embroidered baby dress"></div>
  <div class="stars">★★★★★</div><div class="name">COTTON BOOTIE FOR BOYS</div><div class="desc">Lorem ipsum dolor</div><div class="price">$14.00</div>
  <div class="wish"><svg width="8" height="7" viewBox="0 0 8 7"><path d="M4 7L0.5 3.5A2 2 0 014 1a2 2 0 013.5 2.5z" fill="var(--peach-soft)"/></svg></div><div class="add">+ ADD TO CART</div>
</div>
<div class="abs card" style="left:244px;top:470px">
  <div class="overlay"></div>
  <div class="ov-btn" style="top:12px;background:#36c9d1"><svg width="10" height="10" viewBox="0 0 10 10"><path d="M2 8L8 2M5 2h3v3" stroke="#fff" stroke-width="1.4" fill="none"/></svg></div><div class="ov-label" style="top:40px">QUICK VIEW</div>
  <div class="ov-btn" style="top:48px;background:var(--peach)"><svg width="10" height="10" viewBox="0 0 10 10"><circle cx="5" cy="5" r="3" stroke="#fff" stroke-width="1.4" fill="none"/></svg></div><div class="ov-label" style="top:76px">FULL VIEW</div>
  <div class="ov-btn" style="top:84px;background:var(--teal)"><svg width="10" height="10" viewBox="0 0 10 10"><path d="M2 5h6M5 2v6" stroke="#fff" stroke-width="1.4"/></svg></div><div class="ov-label" style="top:112px">COMPARE</div>
  <div class="stars">★★★★★</div><div class="name">COTTON BOOTIE FOR BOYS</div><div class="desc">Lorem ipsum dolor</div><div class="price">$14.00</div>
  <div class="wish"><svg width="8" height="7" viewBox="0 0 8 7"><path d="M4 7L0.5 3.5A2 2 0 014 1a2 2 0 013.5 2.5z" fill="var(--peach-soft)"/></svg></div><div class="add">+ ADD TO CART</div>
</div>
<div class="abs card" style="left:366px;top:470px">
  <div class="photo ph-bootie" role="img" aria-label="White satin baby booties"></div>
  <div class="badge-sale" style="left:4px;top:4px;background:var(--peach)">SALE!<b>20%</b>OFF</div>
  <div class="stars">★★★★★</div><div class="name">COTTON BOOTIE FOR BOYS</div><div class="desc">Lorem ipsum dolor</div><div class="price">$14.00</div>
  <div class="wish"><svg width="8" height="7" viewBox="0 0 8 7"><path d="M4 7L0.5 3.5A2 2 0 014 1a2 2 0 013.5 2.5z" fill="var(--peach-soft)"/></svg></div><div class="add">+ ADD TO CART</div>
</div>
<div class="abs card" style="left:492px;top:470px">
  <div class="photo ph-bib" role="img" aria-label="White christening bib"></div>
  <div class="stars">★★★★★</div><div class="name">COTTON BOOTIE FOR BOYS</div><div class="desc">Lorem ipsum dolor</div><div class="price">$14.00</div>
  <div class="wish"><svg width="8" height="7" viewBox="0 0 8 7"><path d="M4 7L0.5 3.5A2 2 0 014 1a2 2 0 013.5 2.5z" fill="var(--peach-soft)"/></svg></div><div class="add">+ ADD TO CART</div>
</div>

<div class="abs section-title" style="top:689px">OUR NEWEST ARRIVALS</div>
<div class="abs arrow" style="left:577px;top:688px">‹</div>
<div class="abs arrow" style="left:594px;top:688px">›</div>
<div class="abs section-rule" style="top:706px"></div>

<div class="abs card" style="left:113px;top:720px">
  <div class="photo ph-sash" role="img" aria-label="White tulle dress with pink sash on a dress form"></div>
  <div class="badge-sale" style="left:4px;top:4px;background:#f9b45b">TOP<b style="font-size:6px">RATED</b></div>
  <div class="stars">★★★★★</div><div class="name">COTTON BOOTIE FOR BOYS</div><div class="desc">Lorem ipsum dolor</div><div class="price">$14.00</div>
  <div class="wish"><svg width="8" height="7" viewBox="0 0 8 7"><path d="M4 7L0.5 3.5A2 2 0 014 1a2 2 0 013.5 2.5z" fill="var(--peach-soft)"/></svg></div><div class="add">+ ADD TO CART</div>
</div>
<div class="abs card" style="left:241px;top:720px">
  <div class="photo ph-bootie" role="img" aria-label="White satin baby booties"></div>
  <div class="stars">★★★★★</div><div class="name">COTTON BOOTIE FOR BOYS</div><div class="desc">Lorem ipsum dolor</div><div class="price">$14.00</div>
  <div class="wish"><svg width="8" height="7" viewBox="0 0 8 7"><path d="M4 7L0.5 3.5A2 2 0 014 1a2 2 0 013.5 2.5z" fill="var(--peach-soft)"/></svg></div><div class="add">+ ADD TO CART</div>
</div>
<div class="abs card" style="left:364px;top:720px">
  <div class="photo ph-suit" role="img" aria-label="White boys christening suit with hat"></div>
  <div class="sash"><span>FREE SHIPPING</span></div>
  <div class="stars">★★★★★</div><div class="name">COTTON BOOTIE FOR BOYS</div><div class="desc">Lorem ipsum dolor</div><div class="price">$14.00</div>
  <div class="wish"><svg width="8" height="7" viewBox="0 0 8 7"><path d="M4 7L0.5 3.5A2 2 0 014 1a2 2 0 013.5 2.5z" fill="var(--peach-soft)"/></svg></div><div class="add">+ ADD TO CART</div>
</div>
<div class="abs card" style="left:490px;top:720px">
  <div class="photo ph-bootie" role="img" aria-label="White satin baby booties"></div>
  <div class="stars">★★★★★</div><div class="name">COTTON BOOTIE FOR BOYS</div><div class="desc">Lorem ipsum dolor</div><div class="price">$14.00</div>
  <div class="wish"><svg width="8" height="7" viewBox="0 0 8 7"><path d="M4 7L0.5 3.5A2 2 0 014 1a2 2 0 013.5 2.5z" fill="var(--peach-soft)"/></svg></div><div class="add">+ ADD TO CART</div>
</div>

<section class="abs newsletter">
  <p>Subscribe to newsletter and recieve our new arrivals update weekly.</p>
  <div class="email">Your email</div>
  <div class="signup">SIGN UP</div>
</section>

<footer class="abs footer">
  <div class="fcol" style="left:224px"><h4>COMPANY INFO</h4><ul><li>Contact Us</li><li>Blog</li><li>Shipping &amp;Returns</li><li>RSS Syndication</li><li>Sitemap</li></ul></div>
  <div class="fcol" style="left:357px"><h4>CATEGORIES</h4><ul><li>New Baby</li><li>Christening &amp; Baptism</li><li>Birhday</li><li>Holiday</li><li>Wedding</li></ul></div>
  <div class="fcol" style="left:478px"><h4>BRANDS</h4><ul><li>Pippin</li><li>View all Brands</li></ul></div>
</footer>
</body>
</html>
```